VELNA BROCADE

Project name: “Velna Brocade” website
Objective: To create an elegant website,
intuitive and responsive to present this
what is “Velna Brocade”
See attached specifications.

```html
<!DOCTYPE html>
<html lang="en">
<head>
<meta charset="UTF-8">
<title>Velna Brocade</title>
<link rel="stylesheet" href="https://fonts.googleapis.com/css2?family=Cormorant+Garamond:wght@500;600&family=Inter:wght@400;500&display=swap">
<style>
:root{
  --green:#3d7059;
  --green-dark:#35533a;
  --ink:#1f2a24;
  --muted:#6b7f74;
  --paper:#f8f7f5;
  --mist:#e8eee9;
  --mint:#cfe2d6;
  --line:#dfe6e1;
  --white:#ffffff;
}
*{margin:0;padding:0;box-sizing:border-box}
html,body{width:1200px;height:2319px;overflow:hidden}
body{font-family:"Inter",sans-serif;color:var(--ink);background:var(--paper);position:relative}
.serif{font-family:"Cormorant Garamond",serif;font-weight:500}
section,footer{position:absolute;left:0;width:1200px}
.abs{position:absolute}
.center{left:0;width:1200px;text-align:center}

/* hero */
.hero{top:0;height:546px;color:var(--white);overflow:hidden}
.hero-photo{position:absolute;inset:0;background:
  radial-gradient(ellipse at 40% 30%,rgba(120,160,130,.45),transparent 55%),
  radial-gradient(ellipse at 80% 70%,rgba(90,70,40,.35),transparent 50%),
  linear-gradient(180deg,#2f5a44 0%,#24503a 50%,#1d4432 100%)}
.nav a{color:var(--white);text-decoration:none;font-size:11px;position:absolute;top:48px}
.brand{top:42px;display:flex;flex-direction:column;align-items:center;gap:6px}
.brand-mark{width:40px;height:40px;border:1.5px solid var(--white);border-radius:50%}
.brand-name{font-size:10px;font-weight:500;letter-spacing:1.6px}
.btn-outline-sm{left:892px;top:42px;width:70px;height:22px;border:1px solid var(--white);border-radius:5px;font-size:9px;display:flex;align-items:center;justify-content:center}
.hero h1{top:138px;font-size:58px;line-height:58px;font-weight:600}
.hero-lede{top:282px;left:395px;width:410px;text-align:center;font-size:15px;line-height:20px}
.btn{position:absolute;display:flex;align-items:center;justify-content:center;gap:10px;border-radius:4px;font-size:12px;color:var(--white)}
.btn-primary{background:var(--green)}
.btn-ghost{border:1.2px solid rgba(255,255,255,.85)}
.scroll-cue{left:592px;top:500px;width:16px;height:25px;border:1.5px solid rgba(255,255,255,.8);border-radius:8px}
.scroll-cue::after{content:"";position:absolute;left:6px;top:5px;width:1.5px;height:6px;background:var(--white)}

/* about */
.about{top:546px;height:306px;background:linear-gradient(180deg,#f4f4f1,var(--mist))}
.eyebrow{top:63px;font-size:9px;letter-spacing:1px;color:var(--green);font-weight:500}
.eyebrow-rule{top:80px;left:541px;width:118px;height:1px;background:var(--green);opacity:.6}
h2{font-size:36px;line-height:40px;color:var(--ink)}
.copy{font-size:13px;line-height:17.5px;color:var(--muted)}

/* offer */
.offer{top:852px;height:379px;background:var(--paper)}
.card{top:131px;width:227px;height:188px;background:var(--white);border:1.5px solid var(--line);border-radius:6px;text-align:center}
.card-icon{margin:20px auto 0;width:40px;height:40px;border-radius:50%;background:var(--mint);display:flex;align-items:center;justify-content:center}
.card h3{font-size:16px;margin-top:16px;font-weight:500}
.card p{font-size:10.3px;line-height:16.4px;color:var(--muted);margin:10px 22px 0}

/* discover */
.discover{top:1231px;height:290px;background:linear-gradient(180deg,var(--mist),var(--paper))}

/* why */
.why{top:1521px;height:293px;background:var(--paper)}
.point{width:274px;height:51px;background:#f1f2ef;border:1px solid var(--line);border-radius:4px;display:flex;align-items:center;gap:11px;padding-left:16px;font-size:12px;font-weight:500}
.tick{width:20px;height:20px;border-radius:50%;background:var(--green);display:flex;align-items:center;justify-content:center}

/* join */
.join{top:1814px;height:254px;background:linear-gradient(180deg,#eef1ed,var(--mist))}
.email-field{left:459px;top:167px;width:188px;height:23px;background:var(--paper);border-radius:3px;font-size:8.5px;color:#8a968f;display:flex;align-items:center;padding-left:8px}

/* footer */
.site-footer{top:2068px;height:251px;background:var(--green-dark);color:#e4ebe6}
.foot-head{font-family:"Cormorant Garamond",serif;font-size:11px;font-weight:500;top:43px}
.foot-list{top:70px;font-size:10px;line-height:20px}
.social{top:68px;width:25px;height:25px;border-radius:50%;background:rgba(255,255,255,.14);display:flex;align-items:center;justify-content:center}
.social span{width:9px;height:9px;border:1.3px solid #e4ebe6;border-radius:50%}
.foot-rule{left:168px;top:174px;width:862px;height:1px;background:rgba(255,255,255,.2)}
.copyright{top:197px;font-size:9.5px;color:#c9d4cc}
</style>
</head>
<body>

<section class="hero">
  <div class="hero-photo" role="img" aria-label="Misty forest seen from a wooden veranda with a vase, a bowl and an armchair"></div>
  <nav class="nav">
    <a href="#about" style="left:237px">About</a>
    <a href="#vision" style="left:286px">Vision</a>
    <a href="#contact" style="left:335px">Contact</a>
  </nav>
  <div class="abs brand center">
    <div class="brand-mark"></div>
    <div class="brand-name">VELNA BROCADE</div>
  </div>
  <div class="abs btn-outline-sm">Get in Touch</div>
  <h1 class="abs center serif" style="font-weight:600">Where Nature Meets<br>Refined Living</h1>
  <p class="abs hero-lede">Discover Velna Brocade — a serene retreat designed to reconnect you with land, landscape, and authentic rural charm.</p>
  <div class="btn btn-primary" style="left:453px;top:373px;width:178px;height:31px">Explore Velna Brocade
    <svg width="10" height="10" viewBox="0 0 10 10"><path d="M1 5h8M6 2l3 3-3 3" stroke="#fff" stroke-width="1.2" fill="none"/></svg></div>
  <div class="btn btn-ghost" style="left:642px;top:373px;width:104px;height:31px">Learn More</div>
  <div class="abs scroll-cue"></div>
</section>

<section class="about" id="about">
  <div class="abs center eyebrow">ABOUT VELNA BROCADE</div>
  <div class="abs eyebrow-rule"></div>
  <h2 class="abs center serif" style="top:101px">A Vision of Harmony</h2>
  <p class="abs center copy" style="top:161px">Nestled in the heart of unspoiled countryside, Velna Brocade is a vision of harmony between<br>eco-living and timeless architecture.</p>
  <p class="abs center copy" style="top:211px;color:var(--ink)">Our mission is simple: to create a place where comfort, nature, and community breathe<br>together in perfect balance.</p>
</section>

<section class="offer">
  <h2 class="abs center serif" style="top:55px;font-size:29px">What We Offer</h2>
  <div class="abs card" style="left:237px">
    <div class="card-icon"><svg width="18" height="18" viewBox="0 0 24 24" fill="none" stroke="#3d7059" stroke-width="1.6"><path d="M5 19c0-8 5-13 14-13 0 9-5 13-11 13H5z"/><path d="M5 19l8-8"/></svg></div>
    <h3 class="serif">Sustainable Living</h3>
    <p>Homes and spaces built with ecological materials, respectful of the land and inspired by the region's natural beauty.</p>
  </div>
  <div class="abs card" style="left:486px">
    <div class="card-icon"><svg width="18" height="18" viewBox="0 0 24 24" fill="none" stroke="#3d7059" stroke-width="1.6"><path d="M4 11l8-7 8 7v9H4z"/><path d="M10 20v-6h4v6"/></svg></div>
    <h3 class="serif">Authentic Architecture</h3>
    <p>A blend of modern elegance and traditional rural charm, designed for warmth, light, and longevity.</p>
  </div>
  <div class="abs card" style="left:734px">
    <div class="card-icon"><svg width="18" height="18" viewBox="0 0 24 24" fill="none" stroke="#3d7059" stroke-width="1.6"><path d="M9 4l-5 8h10z"/><path d="M9 12v8"/><path d="M16 9l-3 6h6z"/><path d="M16 15v5"/></svg></div>
    <h3 class="serif">A Connected Landscape</h3>
    <p>Rolling fields, natural pathways, forests, and open spaces — inviting you to slow down and experience life with intention.</p>
  </div>
</section>

<section class="discover" id="vision">
  <h2 class="abs center serif" style="top:57px;font-size:29px">Discover the Velna Brocade Experience</h2>
  <p class="abs center copy" style="top:120px">Whether you seek a peaceful residence, a getaway surrounded by nature, or a meaningful<br>investment in sustainable living, Velna Brocade offers a new way of being — grounded,<br>connected, and inspired by the land.</p>
  <div class="btn btn-primary" style="left:530px;top:185px;width:139px;height:27px;font-size:9px">Explore Our Vision
    <svg width="9" height="9" viewBox="0 0 10 10"><path d="M1 5h8M6 2l3 3-3 3" stroke="#fff" stroke-width="1.2" fill="none"/></svg></div>
</section>

<section class="why">
  <h2 class="abs center serif" style="top:38px;font-size:30px">Why Velna Brocade?</h2>
  <div class="abs point" style="left:318px;top:114px"><span class="tick"><svg width="10" height="10" viewBox="0 0 10 10"><path d="M2 5l2 2 4-4" stroke="#fff" stroke-width="1.4" fill="none"/></svg></span>Thoughtfully designed landscapes</div>
  <div class="abs point" style="left:607px;top:114px"><span class="tick"><svg width="10" height="10" viewBox="0 0 10 10"><path d="M2 5l2 2 4-4" stroke="#fff" stroke-width="1.4" fill="none"/></svg></span>Eco-friendly philosophy</div>
  <div class="abs point" style="left:318px;top:181px"><span class="tick"><svg width="10" height="10" viewBox="0 0 10 10"><path d="M2 5l2 2 4-4" stroke="#fff" stroke-width="1.4" fill="none"/></svg></span>Tranquil, timeless atmosphere</div>
  <div class="abs point" style="left:607px;top:181px"><span class="tick"><svg width="10" height="10" viewBox="0 0 10 10"><path d="M2 5l2 2 4-4" stroke="#fff" stroke-width="1.4" fill="none"/></svg></span>Built for future generations</div>
</section>

<section class="join" id="contact">
  <h2 class="abs center serif" style="top:55px;font-size:31px">Join the Journey</h2>
  <p class="abs center copy" style="top:111px;font-size:11.5px;line-height:17.5px">Be among the first to discover updates, availability, and the unfolding story of<br>Velna Brocade.</p>
  <div class="abs email-field">Enter your email</div>
  <div class="btn btn-primary" style="left:658px;top:166px;width:83px;height:27px;font-size:9px">Subscribe</div>
</section>

<footer class="site-footer">
  <div class="abs" style="left:168px;top:49px;width:96px;display:flex;flex-direction:column;align-items:center;gap:8px">
    <div style="width:46px;height:46px;border:1.5px solid #e4ebe6;border-radius:50%"></div>
    <div style="font-size:10px;font-weight:500;letter-spacing:1.5px;white-space:nowrap">VELNA BROCADE</div>
  </div>
  <div class="abs foot-head" style="left:392px">Quick Links</div>
  <div class="abs foot-list" style="left:392px">Home<br>About<br>Vision<br>Contact</div>
  <div class="abs foot-head" style="left:615px">Get in Touch</div>
  <div class="abs foot-list" style="left:615px">Email: info@velnabrocade.com<br>Phone: +XX XXX XXX XXX<br>Location: Region of Aubrelle</div>
  <div class="abs foot-head" style="left:838px">Follow Us</div>
  <div class="abs social" style="left:838px"><span></span></div>
  <div class="abs social" style="left:873px"><span></span></div>
  <div class="abs social" style="left:908px"><span></span></div>
  <div class="abs foot-rule"></div>
  <div class="abs center copyright">© 2025 Velna Brocade — All Rights Reserved.</div>
</footer>

</body>
</html>
```